Website Refresh Needed - Large Couples Therapy Group

We are a large couples counselling group in Australia, and we have some key pages of our website that need refreshing, as it's a few years old now.
Similar colour palette as currently, and the same colours as the logo. No new logo required.
Total of 7 new (updated) page templates designs are needed:
1. HOME: https://www.velmoraclinic.com.au/
2: CONTACT US: https://www.velmoraclinic.com.au/contact/
3: RC CITY PAGE: https://www.velmoraclinic.com.au/city/sydney/
4: ST CITY PAGE: https://www.velmoraclinic.com.au/our-counselling/sex-therapy/sex-therapy-sydney/
5: ALL BLOGS: https://www.velmoraclinic.com.au/blog/
6: BLOG: https://www.velmoraclinic.com.au/sexual-desires-in-men-and-women-what-are-the-real-differences/
7: MAIN STANDARD PAGE: https://www.velmoraclinic.com.au/our-counselling/couples-relationship-counselling/

Target Market(s)

couples who are going through a crisis in their relationship or marriage.

Number of Pages Required

5+ page

Colors
86cfc6
b8a6cd
cfdfed

Requirements
Must have
• Calm, reassuring colours. People are stressed and need to know we can help.
Should not have
• No bright oranges or yellows.

```html
<!DOCTYPE html>
<html lang="en">
<head>
<meta charset="utf-8">
<title>Velmora Clinic — Relationship &amp; Marriage Counselling</title>
<link rel="stylesheet" href="https://fonts.googleapis.com/css2?family=Montserrat:wght@400;500;600;700&family=Raleway:wght@300;400;500&family=Dancing+Script:wght@500&display=swap">
<style>
:root{
  --teal:#3f9ea7;
  --teal-dark:#35878f;
  --taupe:#6f6561;
  --bar:#776e69;
  --red:#e3262e;
  --ink:#4a4a4a;
  --muted:#8a8a8a;
  --light:#f4f4f4;
  --white:#ffffff;
}
*{box-sizing:border-box;margin:0;padding:0}
html,body{width:1200px;height:4988px;overflow:hidden}
body{position:relative;background:var(--white);font-family:'Montserrat',sans-serif;color:var(--ink)}
.abs{position:absolute}
.ph{position:absolute}

/* top nav */
.topbar{left:0;top:0;width:1200px;height:39px;background:var(--bar);display:flex;justify-content:center;align-items:center;gap:30px}
.topbar a{color:var(--white);font-size:9px;font-weight:600;letter-spacing:.5px;text-decoration:none;text-transform:uppercase}
.topbar a.active{color:#9fd6d9}
.header{left:0;top:39px;width:1200px;height:62px}
.call{left:120px;top:26px;font-size:10px;font-weight:600;color:var(--ink)}
.brand{left:525px;top:14px;display:flex;align-items:center;gap:6px}
.brand .dot{width:22px;height:22px;border-radius:50%;background:var(--teal)}
.brand .name{font-family:'Montserrat',sans-serif;font-size:19px;font-weight:500;color:var(--teal)}
.brand small{display:block;font-size:6px;color:var(--teal);letter-spacing:.3px}
.request{left:898px;top:26px;font-size:8.5px;font-weight:600;color:var(--teal);letter-spacing:.4px}
.search-ico{left:1062px;top:22px}

/* hero */
.hero{left:0;top:101px;width:1200px;height:445px;background:linear-gradient(100deg,#c8a98a 0%,#e8c8a2 30%,#b88f72 55%,#6f7f88 80%,#4a5a66 100%)}
.hero-caption{left:0;top:500px;width:1200px;text-align:center;font-size:8px;letter-spacing:5px;color:var(--white);font-weight:600}
.hero-count{left:1025px;top:500px;font-size:8px;color:var(--white)}
.finder{left:865px;top:172px;width:215px;height:240px;background:var(--teal);padding:20px 18px;color:var(--white)}
.finder h3{font-size:15px;font-weight:500;text-align:center}
.finder .near{font-size:7px;letter-spacing:4px;text-align:center;margin:6px 0 22px;display:flex;align-items:center;gap:6px}
.finder .near:before,.finder .near:after{content:"";flex:1;height:1px;background:rgba(255,255,255,.6)}
.finder .field{font-size:8px;font-weight:600;border-bottom:1px solid rgba(255,255,255,.7);padding:4px 12px 6px;margin:0 0 12px;display:flex;justify-content:space-between}
.finder .btn{margin:18px auto 0;width:164px;height:32px;background:var(--red);font-size:8px;font-weight:700;display:flex;align-items:center;justify-content:center;gap:6px}
.heart{width:10px;height:10px;fill:currentColor}

/* specialise */
.h-teal{left:0;width:1200px;text-align:center;color:var(--teal);font-family:'Raleway',sans-serif;font-weight:500;font-size:24px;letter-spacing:.3px}
.underline{left:565px;width:70px;height:1px;background:#c9c9c9}
.intro-photo{left:199px;top:704px;width:291px;height:380px;background:linear-gradient(160deg,#d8c3a4,#b89a85 55%,#8d9ab2)}
.col{width:214px;font-size:10.5px;line-height:1.95;color:var(--muted)}
.col p{margin-bottom:14px}
.learn{font-size:8.5px;font-weight:600;color:var(--teal);letter-spacing:.5px;display:flex;align-items:center;gap:6px}

/* gallery */
.g{background:#888}
.g-label{left:210px;top:1381px;font-size:13px;font-weight:600;color:var(--white)}

/* therapists */
.h-grey{left:0;width:1200px;text-align:center;font-family:'Raleway',sans-serif;font-weight:400;font-size:25px;color:var(--taupe);letter-spacing:.3px}
.sub{left:0;width:1200px;text-align:center;font-size:13px;color:var(--muted)}
.panel{background:var(--light)}
.issues{list-style:none;font-size:10px;line-height:2;color:var(--muted)}
.issues li:before{content:"";display:inline-block;width:4px;height:4px;border-radius:50%;background:var(--teal);margin-right:6px;vertical-align:middle}
.link-line{height:1px;background:#c8c8c8}
.play{width:56px;height:56px;border-radius:50%;background:var(--white);display:flex;align-items:center;justify-content:center}

/* about */
.about{left:0;top:2537px;width:1200px;height:546px;background:radial-gradient(ellipse at 50% 50%,#4f5650 0%,#2e3530 60%,#1f2621 100%)}
.about h2{position:absolute;left:0;top:120px;width:1200px;text-align:center;color:var(--white);font-family:'Raleway',sans-serif;font-weight:400;font-size:25px}
.about .vision{position:absolute;left:280px;top:198px;width:640px;text-align:center;color:var(--white);font-family:'Dancing Script',cursive;font-size:19px;line-height:1.4}
.about .more{position:absolute;left:0;top:412px;width:1200px;display:flex;justify-content:center;align-items:center;gap:10px;color:#d8d8d8;font-size:8.5px;letter-spacing:.6px}

/* cards */
.card{top:3175px;height:386px}
.card .photo{width:100%;height:192px}
.card .body{position:absolute;left:0;top:192px;width:100%;height:194px;background:var(--taupe);padding:38px 34px;color:var(--white)}
.card h4{font-size:15px;font-weight:600;letter-spacing:.6px;margin-bottom:12px}
.card p{font-size:12px;line-height:1.55;color:#e6e0dd}
.quote{background:var(--teal);padding:48px 38px;color:var(--white)}
.quote .mark{font-size:46px;font-family:'Raleway',sans-serif;line-height:.8;opacity:.8}
.quote p{font-size:14.5px;font-style:italic;line-height:1.65;margin-top:14px}
.quote p b{font-weight:600}
.quote .by{margin-top:22px;font-size:8px;font-weight:700;letter-spacing:.5px;display:flex;align-items:center;gap:8px}
.quote .by:before{content:"";width:22px;height:1px;background:var(--white)}

/* approach */
.approach-photo{left:234px;top:3793px;width:343px;height:319px;background:linear-gradient(150deg,#e8d5bb,#c8a98c 50%,#a88a72)}
.approach-text{left:635px;top:3838px;width:305px;font-size:14.5px;line-height:1.95;color:var(--muted)}
.approach-text:before{content:"";position:absolute;left:-28px;top:14px;width:18px;height:1px;background:#c8c8c8}

/* blogs */
.blogs-h{left:0;top:4212px;width:1200px;text-align:center;font-family:'Raleway',sans-serif;font-size:25px;color:var(--taupe)}
.blogs-h span{color:#b9bcc0}
.post{top:4325px;width:151px}
.post .img{width:151px;height:189px}
.post .date{margin-top:24px;font-size:7.5px;font-weight:600;color:var(--ink);display:flex;align-items:center;gap:8px}
.post .date:before{content:"";width:12px;height:1px;background:#aaa}
.post .title{margin:8px 0 0 20px;font-size:10px;line-height:1.35;color:var(--muted)}

/* footer */
.footer{left:0;top:4718px;width:1200px;height:270px;background:var(--teal);color:var(--white)}
.footer .brand{left:523px;top:76px}
.footer .brand .dot{background:var(--white)}
.footer .brand .name,.footer .brand small{color:var(--white)}
.f-links{left:0;top:128px;width:1200px;display:flex;justify-content:center;gap:14px;font-size:7.5px;font-weight:600}
.f-copy{left:0;top:150px;width:1200px;text-align:center;font-size:7.5px;font-weight:500;letter-spacing:.3px}
.f-social{left:570px;top:186px;display:flex;gap:5px}
.f-social span{width:11px;height:11px;background:var(--white);opacity:.9}
</style>
</head>
<body>

<nav class="abs topbar">
  <a class="active">Home</a><a>About Us</a><a>Counselling Types</a><a>Relationship Counselling Locations</a><a>Sex Therapy Locations</a><a>Quizzes</a><a>Fees &amp; Rebates</a><a>FAQs</a><a>Contact Us</a>
</nav>

<header class="abs header">
  <div class="abs call">CALL : 1300 555 018</div>
  <div class="abs brand"><span class="dot"></span><div><span class="name">Velmora Clinic</span><small>helping you create loving relationships</small></div></div>
  <div class="abs request">›&nbsp;&nbsp; REQUEST AN APPOINTMENT</div>
  <svg class="abs search-ico" width="18" height="18" viewBox="0 0 18 18" fill="none" stroke="#3f9ea7" stroke-width="1.5"><circle cx="7.5" cy="7.5" r="5.5"/><path d="M11.5 11.5l5 5"/></svg>
</header>

<section>
  <div class="abs hero" role="img" aria-label="Photo of a laughing couple embracing outdoors at sunset"></div>
  <div class="abs hero-caption">EXPERT RELATIONSHIP &amp; MARRIAGE COUNSELLING</div>
  <div class="abs hero-count">1 / 4</div>
  <form class="abs finder">
    <h3>Search our Therapists</h3>
    <div class="near">NEAR YOU</div>
    <div class="field"><span>Type of Counselling</span><span>▾</span></div>
    <div class="field"><span>Location</span></div>
    <div class="field"><span>Or Postcode</span></div>
    <div class="btn">SEARCH THERAPISTS <svg class="heart" viewBox="0 0 10 10"><path d="M5 9L1 5A2.3 2.3 0 015 2a2.3 2.3 0 014 3z"/></svg></div>
  </form>
</section>

<section>
  <h1 class="abs h-teal" style="top:610px">WE SPECIALISE IN RELATIONSHIP &amp; MARRIAGE COUNSELLING</h1>
  <div class="abs underline" style="top:654px"></div>
  <div class="abs intro-photo" role="img" aria-label="Portrait photo of a smiling woman"></div>
  <div class="abs col" style="left:532px;top:700px">
    <p>Welcome to the Velmora Clinic... You've come to the right place if you value your relationship, (along with being true to yourself) and would like help with how to repair the inevitable difficulties that come up in most relationships, and build a stronger more authentic connection.</p>
    <p>None of us, when we fall in love, imagine how difficult our relationship is going to be at times. We always hope for the best, then do our best, and still we can find that we can get stranded in problems that we don't really understand. We can unwittingly get into distressing lose-lose negative cycles, and not know how to get out of them cycles, and not know how to get out of them.</p>
  </div>
  <div class="abs col" style="left:784px;top:700px">
    <p>This is perfectly understandable because most of us haven't been taught how to have a great relationship. We're just doing the best we know how.</p>
    <p>There is a very complex blend of science and art in creating great relationships, and this is both our passion and specialty.</p>
    <p>We're a group of nearly 100 psychologists, counsellors and sex therapists Australia wide who are passionate about relationships; understanding what makes them tick, how to best overcome difficulties, how to communicate effectively, how to get your relationship back on track, and even build new depths of compassion, understanding and honesty.</p>
  </div>
  <div class="abs learn" style="left:542px;top:1140px">LEARN MORE <svg class="heart" viewBox="0 0 10 10"><path d="M5 9L1 5A2.3 2.3 0 015 2a2.3 2.3 0 014 3z"/></svg></div>
</section>

<section>
  <div class="ph g" style="left:100px;top:1244px;width:386px;height:165px;background:linear-gradient(135deg,#6a2f3a,#b8607a 50%,#4a2a3a)" role="img" aria-label="Photo of a wedding couple under festive lights"></div>
  <div class="abs g-label">Relationship Counselling</div>
  <div class="ph g" style="left:493px;top:1244px;width:213px;height:165px;background:linear-gradient(180deg,#9a8a7a,#5a6a78 55%,#3e4f5a)" role="img" aria-label="Photo of a couple embracing in the sea"></div>
  <div class="ph g" style="left:714px;top:1244px;width:386px;height:165px;background:linear-gradient(180deg,#f2f2f2,#e2e2e2)" role="img" aria-label="Photo of a person curled up on a white floor"></div>
  <div class="ph g" style="left:100px;top:1416px;width:606px;height:227px;background:linear-gradient(160deg,#8a5a30,#3a3f5a 50%,#c9c4c0)" role="img" aria-label="Photo of guests celebrating a wedding couple"></div>
  <div class="ph g" style="left:714px;top:1416px;width:386px;height:227px;background:linear-gradient(180deg,#b8d0a0,#7fae5c 60%,#5c8e3e)" role="img" aria-label="Photo of two decorated wedding chairs on a lawn"></div>
</section>

<section>
  <h2 class="abs h-grey" style="top:1728px">OUR RELATIONSHIP THERAPISTS</h2>
  <div class="abs sub" style="top:1771px">Can help with the following common relationship issues, and more</div>

  <div class="abs panel" style="left:557px;top:1852px;width:441px;height:302px"></div>
  <div class="ph" style="left:607px;top:1889px;width:347px;height:232px;background:linear-gradient(100deg,#d8b088,#c9906a 40%,#5a6e7a)" role="img" aria-label="Video still of a couple laughing outdoors"></div>
  <div class="abs play" style="left:752px;top:1977px"><svg width="16" height="18" viewBox="0 0 16 18"><path d="M2 1l13 8-13 8z" fill="#3f9ea7"/></svg></div>
  <ul class="abs issues" style="left:331px;top:1950px"><li>Affairs</li><li>Controlling behaviour</li><li>Verbal abuse</li><li>Imbalance of power</li><li>Lack of intimacy</li><li>Poor communication</li><li>Loss of love</li></ul>
  <div class="abs link-line" style="left:534px;top:1960px;width:48px"></div>

  <div class="abs panel" style="left:199px;top:2158px;width:441px;height:301px"></div>
  <div class="ph" style="left:250px;top:2192px;width:346px;height:233px;background:linear-gradient(90deg,#d8c4b4,#f0ece8 50%,#d6d2ce)" role="img" aria-label="Video still of a couple standing back to back"></div>
  <div class="abs play" style="left:389px;top:2281px"><svg width="16" height="18" viewBox="0 0 16 18"><path d="M2 1l13 8-13 8z" fill="#3f9ea7"/></svg></div>
  <ul class="abs issues" style="left:708px;top:2236px"><li>Relationship neglect</li><li>Sexual problems</li><li>Problems from childhood</li><li>Problems with parenting your children</li><li>Step children and in-laws</li><li>All forms of family problems</li><li>Anger management problems</li></ul>
  <div class="abs link-line" style="left:623px;top:2245px;width:48px"></div>
</section>

<section class="abs about" role="img" aria-label="Background photo of a wedding couple among greenery">
  <h2>ABOUT VELMORA CLINIC</h2>
  <p class="vision">Our vision is to be the most highly regarded and comprehensive marriage counselling, relationship counselling and sex therapy service in Australia, at reasonable and affordable rates. We hand choose our team of Registered Psychologists, Counsellors and Sex Therapists considering their knowledge, compassion, and unbiased approach to marriage counselling and sexual therapy and their experience in the relationship field.</p>
  <div class="more">LEARN <svg class="heart" viewBox="0 0 10 10" style="fill:#fff;width:14px;height:14px"><path d="M5 9L1 5A2.3 2.3 0 015 2a2.3 2.3 0 014 3z"/></svg> MORE</div>
</section>

<section>
  <div class="abs card" style="left:199px;width:262px">
    <div class="photo" role="img" aria-label="Photo of a couple about to kiss" style="background:linear-gradient(150deg,#e6d4c0,#b89a84)"></div>
    <div class="body">
      <h4>REBATES AVAILABLE</h4>
      <p>You may be able to receive rebates of up to 75% of your session costs.</p>
    </div>
  </div>
  <div class="abs card" style="left:468px;width:263px">
    <div class="photo" role="img" aria-label="Photo of a wedding couple seated by the coast" style="background:linear-gradient(180deg,#c8ccd0,#9aa2a8 50%,#e8e4e2)"></div>
    <div class="body">
      <h4>SATISFACTION<br>GUARANTEE</h4>
      <p>We're proud to offer our 100% risk-free, satisfaction guarantee.</p>
      <svg class="abs" style="left:205px;top:32px" width="36" height="34" viewBox="0 0 36 34" fill="none" stroke="#fff" stroke-width="1.5"><path d="M3 15h6v16H3zM9 17l6-10c1-3 5-2 4 2l-2 6h11c2 0 3 2 2 4l-3 10c-1 2-2 2-4 2H9"/></svg>
    </div>
  </div>
  <div class="abs card quote" style="left:737px;width:261px">
    <div class="mark">&ldquo;</div>
    <p><b>Connection</b> is the energy between people when they feel seen, heard, and valued; when they can give and recieve without judgement; and when they get sustenance and strength from the relationship.</p>
    <div class="by">MARA ELLISON</div>
  </div>
</section>

<section>
  <h2 class="abs h-grey" style="top:3681px">OUR MARRIAGE COUNSELLING APPROACH</h2>
  <div class="abs underline" style="left:588px;top:3750px;width:24px"></div>
  <svg class="abs" style="left:122px;top:3925px" width="24" height="50" viewBox="0 0 24 50" fill="none" stroke="#3f9ea7" stroke-width="1.5"><path d="M22 2L2 25l20 23"/></svg>
  <div class="abs approach-photo" role="img" aria-label="Photo of a couple touching foreheads"></div>
  <p class="abs approach-text">It is very important to us that we take a very positive approach to relationship counselling. From your very first session, we will take the time to fully understand each of your individual perspectives, without bias, and get to the very root of the issues that are affecting your relationship.</p>
  <svg class="abs" style="left:998px;top:3905px" width="24" height="50" viewBox="0 0 24 50" fill="none" stroke="#3f9ea7" stroke-width="1.5"><path d="M2 2l20 23L2 48"/></svg>
</section>

<section>
  <h2 class="abs blogs-h">BLOGS &nbsp;/&nbsp; <span>NEWS</span></h2>
  <article class="abs post" style="left:134px"><div class="img" role="img" aria-label="Photo of a bride and groom" style="background:linear-gradient(160deg,#6a5a4e,#c8b8a8)"></div><div class="date">30 AUG 2020</div><div class="title">What is Borderline Personality Disorder and how does it affect my</div></article>
  <article class="abs post" style="left:290px"><div class="img" role="img" aria-label="Photo of a couple on a city rooftop" style="background:linear-gradient(160deg,#8a8e92,#d0ccc8)"></div><div class="date">30 AUG 2020</div><div class="title">What is Borderline Personality Disorder and how does it affect my</div></article>
  <article class="abs post" style="left:447px"><div class="img" role="img" aria-label="Photo of a bride in a lace gown" style="background:linear-gradient(160deg,#b48aa0,#ece2e6)"></div><div class="date">30 AUG 2020</div><div class="title">What is Borderline Personality Disorder and how does it affect my</div></article>
  <article class="abs post" style="left:604px"><div class="img" role="img" aria-label="Black and white photo of a couple embracing" style="background:linear-gradient(160deg,#9a9a9a,#e0e0e0)"></div><div class="date">30 AUG 2020</div><div class="title">What is Borderline Personality Disorder and how does it affect my</div></article>
  <article class="abs post" style="left:760px"><div class="img" role="img" aria-label="Photo of a couple dancing outdoors" style="background:linear-gradient(180deg,#a8b8c4,#8a9a7a)"></div><div class="date">30 AUG 2020</div><div class="title">What is Borderline Personality Disorder and how does it affect my</div></article>
  <article class="abs post" style="left:917px"><div class="img" role="img" aria-label="Photo of hands holding with a bouquet" style="background:linear-gradient(160deg,#d8a0b0,#6e8e5e)"></div><div class="date">30 AUG 2020</div><div class="title">What is Borderline Personality Disorder and how does it affect my</div></article>
</section>

<footer class="abs footer">
  <div class="abs brand"><span class="dot"></span><div><span class="name">Velmora Clinic</span><small>helping you create loving relationships</small></div></div>
  <div class="abs f-links"><span>HOME</span><span>ABOUT US</span><span>OUR BLOGS</span><span>MEMBERS</span><span>LOG IN</span><span>CONTACT US</span></div>
  <div class="abs f-copy">© COPYRIGHT 2020 &nbsp;//&nbsp; TERMS AND POLICY &nbsp;//&nbsp; WWW.VELMORACLINIC.COM.AU</div>
  <div class="abs f-social"><span></span><span></span><span></span><span></span></div>
</footer>

</body>
</html>
```